Accounting firm needing business card / letterhead designed
Marcus T. Elbering, CPA
marcus@fernquill.com
www.fernquill.com
482 N Harlow Ave Alder Falls, MN 43719
208-555-0172

```html
<!DOCTYPE html>
<html lang="en">
<head>
<meta charset="utf-8">
<title>Fernquill Business Card</title>
<link rel="stylesheet" href="https://fonts.googleapis.com/css2?family=Barlow+Semi+Condensed:wght@500;700&family=Barlow:wght@500&display=swap">
<style>
  :root {
    --page: #e6e6e6;
    --card-light: #f4f4f4;
    --card-light-edge: #e9e9e9;
    --navy: #21124a;
    --green: #5db12c;
    --ink: #1c1c28;
    --white: #f2f2f2;
  }
  * { box-sizing: border-box; margin: 0; padding: 0; }
  html, body {
    width: 1200px; height: 576px; overflow: hidden;
    background: var(--page);
  }
  .canvas { position: relative; width: 1200px; height: 576px; }
  .card {
    position: absolute;
    border-radius: 13px;
    overflow: hidden;
  }
  .card--front {
    left: 82px; top: 139px; width: 485px; height: 293px;
    background: linear-gradient(160deg, var(--card-light) 0%, var(--card-light-edge) 100%);
  }
  .card--back {
    left: 602px; top: 138px; width: 480px; height: 291px;
    background: var(--navy);
  }
  .holder-name {
    position: absolute; left: 29px; top: 39px;
    font-family: "Barlow Semi Condensed", sans-serif;
    font-weight: 700; font-size: 19px; line-height: 22px; color: var(--navy);
    letter-spacing: 0.1px;
  }
  .holder-name .credential { color: var(--green); }
  .contact-list {
    position: absolute; left: 29px; top: 67px;
    list-style: none;
    font-family: "Barlow Semi Condensed", sans-serif;
    font-weight: 500; font-size: 12.5px; color: var(--ink);
  }
  .contact-item { display: flex; align-items: center; height: 15.5px; }
  .contact-icon { width: 11px; height: 11px; margin-right: 13px; flex: none; }
  .address {
    position: absolute; left: 29px; top: 117px;
    font-family: "Barlow Semi Condensed", sans-serif;
    font-weight: 500; font-size: 12.5px; line-height: 15px; color: var(--ink);
  }
  .brand-name {
    position: absolute;
    font-family: "Barlow", sans-serif;
    font-weight: 500; font-size: 34px; letter-spacing: 3px;
    line-height: 1;
  }
  .card--front .brand-name { left: 29px; top: 223px; color: var(--navy); }
  .card--back .brand-name { right: 36px; top: 215px; color: var(--white); }
</style>
</head>
<body>
<div class="canvas">
  <section class="card card--front" aria-label="Business card front">
    <h1 class="holder-name">Marcus T. Elbering, <span class="credential">CPA</span></h1>
    <ul class="contact-list">
      <li class="contact-item">
        <svg class="contact-icon" viewBox="0 0 12 12" aria-hidden="true"><path fill="#5db12c" d="M1 3.2C1 2 3 1.2 6 1.2s5 .8 5 2V4.4H8.6V3.4H3.4v1H1zM3.2 5h5.6l1.6 5.6H1.6z"/><circle cx="6" cy="7.6" r="1.3" fill="#f4f4f4"/></svg>
        <span>208-555-0172</span>
      </li>
      <li class="contact-item">
        <svg class="contact-icon" viewBox="0 0 12 12" aria-hidden="true"><rect x="0.5" y="2.2" width="11" height="7.6" fill="#5db12c"/><path d="M0.8 2.6 6 6.6l5.2-4" fill="none" stroke="#f4f4f4" stroke-width="1"/></svg>
        <span>marcus@fernquill.com</span>
      </li>
      <li class="contact-item">
        <svg class="contact-icon" viewBox="0 0 12 12" aria-hidden="true"><circle cx="6" cy="6" r="5.3" fill="#5db12c"/><g fill="none" stroke="#f4f4f4" stroke-width="0.7"><ellipse cx="6" cy="6" rx="2.2" ry="5.3"/><path d="M0.7 6h10.6M1.6 3.3h8.8M1.6 8.7h8.8"/></g></svg>
        <span>www.fernquill.com</span>
      </li>
    </ul>
    <p class="address">482 N Harlow Ave Alder Falls, MN 43719</p>
    <p class="brand-name">FERNQUILL</p>
  </section>
  <section class="card card--back" aria-label="Business card back">
    <p class="brand-name">FERNQUILL</p>
  </section>
</div>
</body>
</html>
```